New Business Cards for 3 companies - print and digital Needed FAST!

We have rebranded our company into three separate companies.
We need new business cards for 8 employees, three of whom need a business card for each company - total of 12 cards.
Pelmary is our property development company.
Velta Brokerage & Management handles property management and real estate transactions.
Oakwren Design Build is our construction company.
Business cards MUST be able to be both printed and function as digital business cards.
No black backgrounds.
Front should be each employee's information and include the logo from their primary company.
Back should include all three logos.
Please see the uploaded spreadsheet for all the information you need for each card. Also uploaded the .png files for each logo as well as the style guide for each logo.

Contact Information for Business Card

See uploaded spreadsheet for information

Font styles to use
Sans Serif
Other font styles liked:
• match style guide if possible

Requirements
Should not have
• No dark backgrounds on the front (on the back OK.) No pictures of employees. Thanks!

```html
<!DOCTYPE html>
<html lang="en">
<head>
<meta charset="utf-8">
<title>Pelmary Business Card</title>
<link rel="stylesheet" href="https://fonts.googleapis.com/css2?family=Arimo:wght@400;700&family=Montserrat:wght@500;600&display=swap">
<style>
  :root {
    --stage: #5b5b5b;
    --paper: #ffffff;
    --ink: #3f3f41;
    --band: #444446;
    --green: #72d447;
    --light: #ffffff;
  }
  * { margin: 0; padding: 0; box-sizing: border-box; }
  html, body { width: 1075px; height: 1200px; overflow: hidden; }
  body { background: var(--stage); position: relative; font-family: "Arimo", Arial, sans-serif; color: var(--ink); }

  .card {
    position: absolute; left: 206px; width: 664px; height: 396px;
    background: var(--paper); overflow: hidden;
    box-shadow: 3px 3px 2px rgba(0,0,0,0.55);
  }
  .card--front { top: 187px; }
  .card--back { top: 638px; }

  .company { position: absolute; font-family: "Montserrat", sans-serif; color: var(--ink); }
  .company__name { font-weight: 600; line-height: 1; }
  .company__line { font-weight: 600; margin-top: 10px; }

  .front-company { right: 42px; top: 86px; text-align: right; }
  .front-company .company__name { font-size: 50px; letter-spacing: 1px; }
  .front-company .company__line { font-size: 15px; letter-spacing: 3px; margin-top: 14px; }

  .holder { position: absolute; left: 35px; top: 222px; }
  .holder__name { font-size: 23px; font-weight: 700; line-height: 1.1; }
  .holder__role { font-size: 16px; line-height: 1.2; letter-spacing: 0.2px; }
  .holder__bar { position: absolute; left: 35px; top: 276px; width: 211px; height: 5px; background: var(--green); z-index: 2; }

  .band { position: absolute; left: 0; top: 279px; width: 100%; height: 117px; background: var(--band); color: var(--light); }
  .contacts { position: absolute; left: 35px; top: 22px; list-style: none; font-size: 18px; line-height: 23.5px; }
  .contacts li { display: flex; align-items: center; }
  .contacts svg { width: 17px; height: 17px; margin-right: 6px; flex: none; }
  .address { position: absolute; right: 42px; top: 51px; text-align: right; font-size: 18px; line-height: 23.5px; }

  .frame { position: absolute; left: 39px; top: 46px; width: 584px; height: 318px; border: 4px solid var(--ink); }
  .back-oakwren { left: 152px; top: 106px; text-align: center; }
  .back-oakwren .company__name { font-size: 34px; }
  .back-oakwren .company__line { font-size: 11px; letter-spacing: 3px; margin-top: 8px; }
  .back-velta { left: 342px; top: 106px; text-align: center; }
  .back-velta .company__name { font-size: 34px; letter-spacing: 2px; }
  .back-velta .company__line { font-size: 11px; letter-spacing: 1.3px; margin-top: 8px; }
  .back-pelmary { left: 0; width: 100%; top: 232px; text-align: center; }
  .back-pelmary .company__name { font-size: 44px; letter-spacing: 1px; }
  .back-pelmary .company__line { font-size: 13px; letter-spacing: 3px; margin-top: 12px; }
</style>
</head>
<body>

<section class="card card--front" aria-label="Card front">
  <div class="company front-company">
    <div class="company__name">Pelmary</div>
    <div class="company__line">PROPERTY DEVELOPMENT</div>
  </div>

  <div class="holder">
    <div class="holder__name">DANIEL MERCER</div>
    <div class="holder__role">MANAGING DIRECTOR</div>
  </div>
  <div class="holder__bar"></div>

  <div class="band">
    <ul class="contacts">
      <li>
        <svg viewBox="0 0 24 24" aria-hidden="true"><path fill="#72d447" d="M6.6 10.8c1.4 2.8 3.8 5.1 6.6 6.6l2.2-2.2c.3-.3.7-.4 1-.2 1.1.4 2.3.6 3.6.6.6 0 1 .4 1 1V20c0 .6-.4 1-1 1C10.6 21 3 13.4 3 4c0-.6.4-1 1-1h3.5c.6 0 1 .4 1 1 0 1.3.2 2.5.6 3.6.1.3 0 .7-.2 1z"/></svg>
        044-555 210 347
      </li>
      <li>
        <svg viewBox="0 0 24 24" aria-hidden="true"><path fill="#72d447" d="M2 5h20v14H2z"/><path fill="none" stroke="#444446" stroke-width="1.6" d="M2 5l10 8 10-8M2 19l7-7M22 19l-7-7"/></svg>
        info@pelmary.com
      </li>
      <li>
        <svg viewBox="0 0 24 24" aria-hidden="true"><circle cx="12" cy="12" r="10" fill="#72d447"/><g fill="none" stroke="#444446" stroke-width="1.3"><ellipse cx="12" cy="12" rx="4.5" ry="10"/><path d="M2 12h20M4 7h16M4 17h16M12 2v20"/></g></svg>
        www.pelmary.com
      </li>
    </ul>
    <div class="address">421, Address line goes here<br>45452,Country Name</div>
  </div>
</section>

<section class="card card--back" aria-label="Card back">
  <div class="frame"></div>

  <div class="company back-oakwren">
    <div class="company__name">Oakwren</div>
    <div class="company__line">DESIGN | BUILD</div>
  </div>

  <div class="company back-velta">
    <div class="company__name">Velta</div>
    <div class="company__line">BROKERAGE | MANAGEMENT</div>
  </div>

  <div class="company back-pelmary">
    <div class="company__name">Pelmary</div>
    <div class="company__line">PROPERTY DEVELOPMENT</div>
  </div>
</section>

</body>
</html>
```